Company Gift Card Designs

I would like to have 2 gift cards designed.

Both cards need to be in our company colors and have a non-white background. Both will need to follow the attached spec sheet from the card vendor.

Card 1 - will need to have the words Thank you on the card and use the KTB Logo

Card 2 - will need to have both the KTB logo and the Zel480 Logo incorporated into the design.

```html
<!DOCTYPE html>
<html lang="en">
<head>
<meta charset="utf-8">
<title>KTB Gift Cards</title>
<link rel="stylesheet" href="https://fonts.googleapis.com/css2?family=Titillium+Web:wght@300;400;700;900&display=swap">
<style>
  :root {
    --page: #ffffff;
    --brand-red: #c21f26;
    --brand-red-deep: #b5151b;
    --brand-blue: #2b8bc2;
    --brand-blue-deep: #2581b8;
    --frame: #5a2e17;
    --gold-dark: #8a5a1c;
    --gold-mid: #c99a3e;
    --gold-light: #f6d27a;
    --night: #14243a;
    --night-amber: #3b2c1e;
    --night-deep: #0a1526;
    --white: #ffffff;
    --ink: #1a1a1a;
  }
  * { box-sizing: border-box; margin: 0; padding: 0; }
  html, body {
    width: 1200px;
    height: 2291px;
    overflow: hidden;
    background: var(--page);
    font-family: "Titillium Web", sans-serif;
  }
  .gift-card {
    position: absolute;
    left: 100px;
    width: 1000px;
    height: 630px;
    border: 4px solid var(--frame);
    box-shadow: 0 6px 14px rgba(0,0,0,0.28);
    overflow: hidden;
    background: var(--night);
  }
  .gift-card--thanks { top: 420px; }
  .gift-card--partner { top: 1260px; }

  .brand-panel {
    position: absolute;
    left: 0; top: 0; bottom: 0;
    width: 578px;
    background: var(--brand-red);
    color: var(--white);
  }
  .gift-card--partner .brand-panel {
    width: 595px;
    background: var(--brand-blue);
  }

  .panel-decor {
    position: absolute;
    border-radius: 18px;
    background: var(--brand-red-deep);
  }
  .gift-card--partner .panel-decor { background: var(--brand-blue-deep); }
  .panel-decor--ribbon { left: 344px; top: 12px; width: 178px; height: 180px; }
  .panel-decor--flame { left: 330px; top: 470px; width: 186px; height: 160px; border-radius: 90px 90px 0 0; }
  .panel-decor--gifts { left: 44px; top: 580px; width: 126px; height: 50px; border-radius: 8px 8px 0 0; }

  .brand-mark {
    position: absolute;
    left: 38px; top: 58px;
    font-weight: 900;
    font-size: 96px;
    line-height: 1;
    letter-spacing: -1px;
  }
  .card-headline {
    position: absolute;
    left: 38px; top: 226px;
    font-weight: 700;
    font-size: 90px;
    line-height: 1;
    letter-spacing: 1px;
    white-space: nowrap;
  }
  .card-message {
    position: absolute;
    left: 46px; top: 336px;
    width: 470px;
    font-weight: 400;
    font-size: 21px;
    line-height: 1.2;
  }
  .company-block {
    position: absolute;
    left: 46px; top: 452px;
    font-size: 34px;
    line-height: 0.95;
    letter-spacing: 1px;
  }
  .company-block__light { display: block; font-weight: 300; }
  .company-block__bold { display: block; font-weight: 700; }
  .company-rule {
    position: absolute;
    left: 46px; top: 530px;
    width: 224px; height: 8px;
  }

  .gift-ribbon {
    position: absolute;
    top: 0; bottom: 0;
    left: 578px;
    width: 58px;
    background: linear-gradient(90deg, var(--gold-dark) 0%, var(--gold-mid) 25%, var(--gold-light) 50%, var(--gold-mid) 75%, var(--gold-dark) 100%);
  }
  .gift-card--partner .gift-ribbon { left: 595px; }

  .night-scene {
    position: absolute;
    top: 0; bottom: 0; right: 0;
    left: 636px;
    background: linear-gradient(165deg, var(--night) 0%, var(--night-amber) 55%, var(--night-deep) 100%);
  }
  .gift-card--partner .night-scene { left: 653px; }

  .gift-bow {
    position: absolute;
    width: 220px; height: 186px;
    border-radius: 24px;
    background: linear-gradient(160deg, var(--gold-light) 0%, var(--gold-mid) 55%, var(--gold-dark) 100%);
  }
  .gift-card--thanks .gift-bow { left: 497px; top: 388px; }
  .gift-card--partner .gift-bow { left: 514px; top: 330px; }

  .partner-tag {
    position: absolute;
    right: 0; bottom: 0;
    width: 339px; height: 60px;
    background: var(--white);
    display: flex;
    align-items: center;
    justify-content: center;
    color: var(--ink);
    font-weight: 700;
    font-size: 48px;
    line-height: 1;
  }
</style>
</head>
<body>

<section class="gift-card gift-card--thanks">
  <div class="brand-panel">
    <div class="panel-decor panel-decor--ribbon" role="img" aria-label="Faint ribbon curl illustration"></div>
    <div class="panel-decor panel-decor--flame" role="img" aria-label="Faint flame illustration"></div>
    <div class="panel-decor panel-decor--gifts" role="img" aria-label="Faint gift box illustrations"></div>
    <div class="brand-mark">KTB</div>
    <h1 class="card-headline">THANK YOU</h1>
    <p class="card-message">Lorem Ipsum is simply dummy text of the printing and typesetting industry.</p>
    <div class="company-block">
      <span class="company-block__light">KEYSTONE</span>
      <span class="company-block__bold">TRIBASIN</span>
    </div>
    <svg class="company-rule" viewBox="0 0 224 8" aria-hidden="true">
      <polygon points="0,1 224,0 224,2 0,8" fill="#ffffff"/>
    </svg>
  </div>
  <div class="gift-ribbon"></div>
  <div class="night-scene" role="img" aria-label="Photo of a full moon behind a tree with amber foliage in a starry night sky"></div>
  <div class="gift-bow" role="img" aria-label="Gold satin gift bow illustration"></div>
</section>

<section class="gift-card gift-card--partner">
  <div class="brand-panel">
    <div class="panel-decor panel-decor--ribbon" role="img" aria-label="Faint ribbon curl illustration"></div>
    <div class="panel-decor panel-decor--flame" role="img" aria-label="Faint water drop illustration"></div>
    <div class="panel-decor panel-decor--gifts" role="img" aria-label="Faint gift box illustrations"></div>
    <div class="brand-mark">KTB</div>
    <h1 class="card-headline">THANK YOU</h1>
    <p class="card-message">Lorem Ipsum is simply dummy text of the printing and typesetting industry.</p>
    <div class="company-block">
      <span class="company-block__light">KEYSTONE</span>
      <span class="company-block__bold">TRIBASIN</span>
    </div>
    <svg class="company-rule" viewBox="0 0 224 8" aria-hidden="true">
      <polygon points="0,1 224,0 224,2 0,8" fill="#ffffff"/>
    </svg>
  </div>
  <div class="gift-ribbon"></div>
  <div class="night-scene" role="img" aria-label="Photo of a full moon behind a tree with amber foliage in a starry night sky"></div>
  <div class="partner-tag">ZEL480</div>
  <div class="gift-bow" role="img" aria-label="Gold satin gift bow illustration"></div>
</section>

</body>
</html>
```